Book Cover for Content Marketing Design Process that Targets Creative Entreprenuers

Book Cover for Kindle and print. I like the design I have which I attached, but want the professional touch. The book takes readers through a 3-day creative process to design a written content management strategy for their product or service. It's very experiential, and uses a playful guiding metaphor throughout. Despite the playful non-linear approach, the result is a very comprehensive and practical content plan that puts value and authentic service to customers first.

The message the cover should convey is that it's possible for the business owner to attract the attention of customers, to generate excitement, and to connect with an audience on an emotional level. I estimate the book spine to be around 0.30" on a 6" x 9" cover. For Kindle, the imaged needs to be 2,560 x 1,600 JPG format, no more than 50MB.

Target Market(s)

Creative entrepreneurs, artists, artisans who sell online.

Industry/Entity Type

Consulting

Requirements
Must have
• This is a very creative, spiritual, energetic approach to content marketing. I would like the cover to set the stage for the experiential and creative process to come. Should appear bold and fun.
Nice to have
• What I like about the file attached: the expressive faces highlighting the idea of getting attention and attracting an audience, the playful font for "Playbook," the color scheme. I think the subtitle is important, but not sure if it should be on the cover or not.
Should not have
• Nothing that veers into child-like.

```html
<!DOCTYPE html>
<html lang="en">
<head>
<meta charset="utf-8">
<title>Content Marketing Plybook — Front Cover</title>
<link rel="stylesheet" href="https://fonts.googleapis.com/css2?family=Roboto:wght@300;400;700;900&display=swap">
<style>
  :root {
    --stage: #ecebe8;
    --sky: #5ec3e6;
    --sky-mid: #a9dff1;
    --paper: #ffffff;
    --ink: #1d2226;
    --ink-soft: #2f3a40;
    --glow: 255,255,255;
    --page-shade: 170,182,190;
  }
  * { margin: 0; padding: 0; box-sizing: border-box; }
  html, body { width: 1200px; height: 800px; overflow: hidden; }
  body {
    background: var(--stage);
    font-family: "Roboto", Arial, sans-serif;
    position: relative;
  }
  .cover {
    position: absolute;
    left: 360px; top: 40px;
    width: 480px; height: 720px;
    background: linear-gradient(180deg, var(--sky) 0%, var(--sky-mid) 38%, #e4f4fa 66%, var(--paper) 100%);
    box-shadow: 0 10px 30px rgba(0,0,0,0.18);
    overflow: hidden;
    color: var(--ink);
    text-align: center;
  }
  .tagline {
    position: absolute; left: 0; right: 0; top: 44px;
    font-weight: 300; font-size: 25px; line-height: 29px;
    text-transform: uppercase; color: var(--ink-soft);
  }
  .promise {
    position: absolute; left: 0; right: 0; top: 108px;
    font-weight: 700; font-size: 34px; line-height: 42px;
    text-transform: uppercase; color: var(--ink);
  }
  .promise .small { font-size: 24px; font-weight: 400; }
  .letter-burst {
    position: absolute; left: 0; right: 0; top: 190px; height: 330px;
    background: radial-gradient(closest-side at 50% 80%,
      rgba(var(--glow),0.95) 0%,
      rgba(var(--glow),0.55) 40%,
      rgba(var(--glow),0.15) 75%,
      rgba(var(--glow),0) 100%);
  }
  .topics { list-style: none; }
  .topic {
    position: absolute; left: 0; right: 0;
    text-transform: uppercase; color: var(--ink);
  }
  .topic--product { top: 326px; font-size: 14px; letter-spacing: 4px; }
  .topic--marketing { top: 370px; font-size: 15px; letter-spacing: 5px; }
  .topic--accounting { top: 414px; font-size: 11px; letter-spacing: 3px; }
  .topic--branding { top: 452px; font-size: 10px; letter-spacing: 3px; }
  .open-book {
    position: absolute; left: 90px; width: 300px; top: 430px; height: 80px;
    background: radial-gradient(closest-side at 50% 70%,
      rgba(var(--page-shade),0.5) 0%,
      rgba(var(--page-shade),0.25) 55%,
      rgba(var(--page-shade),0) 100%);
  }
  .title {
    position: absolute; left: 0; right: 0; top: 488px;
    text-transform: uppercase; color: var(--ink);
  }
  .title span { display: block; }
  .title__lead { font-weight: 900; font-size: 66px; line-height: 62px; letter-spacing: -1px; }
  .title__mid { font-weight: 300; font-size: 52px; line-height: 54px; }
  .title__end { font-weight: 300; font-size: 60px; line-height: 62px; color: var(--ink-soft); }
  .subtitle {
    position: absolute; left: 0; right: 0; top: 676px;
    font-weight: 300; font-size: 20px; line-height: 24px;
    text-transform: uppercase; color: var(--ink-soft);
  }
</style>
</head>
<body>
  <main class="cover">
    <p class="tagline">Attract more attention<br>online with</p>
    <p class="promise"><span class="small">A</span> Content Strategy<br><span class="small">That's</span> Fun, Magnetic</p>
    <div class="letter-burst" role="img" aria-label="Swirl of scattered letters rising from an open book"></div>
    <ul class="topics">
      <li class="topic topic--product">Product Development</li>
      <li class="topic topic--marketing">Marketing</li>
      <li class="topic topic--accounting">Accounting</li>
      <li class="topic topic--branding">Branding</li>
    </ul>
    <div class="open-book" role="img" aria-label="Open book with fanned pages"></div>
    <h1 class="title">
      <span class="title__lead">Content</span>
      <span class="title__mid">Marketing</span>
      <span class="title__end">Plybook</span>
    </h1>
    <p class="subtitle">And straight from the heart</p>
  </main>
</body>
</html>
```